Luxury Wine Label for New Startup Winery

We need a wine label for our new winery startup. We have worked with a local designer but do not feel the resulting label / logo have the elevation required to present our brand as a luxury wine. Our winery is called "Harrowgate Vineyards" and we are focused on extremely high quality hand crafted artisan and estate wines from the Pacific Northwest.
We would like to see designs that utilize a tree line, or other imagery that represents the "Harrowgate" part of our company name. Another interesting feature could be wood grain.
A logo will be required based on your design so please design with this in mind:
This logo should be consistent with the wine bottle label design, and should be representative of our high end exclusive wine while giving a sense of place (Oregon/ Pacific Northwest.)
I will supply an image of the design we received from our local designer, PLEASE NOTE: in general we do like wood grain and tree line concepts but feel the execution was poorly done.
ATTN: Logo design should be suitable for use on: Bottles (Red wine/rose/white wine), Bussiness cards, vehicle signage, business signage, etc
P.S.:
If you have a design that is not outside the box we are still interested in seeing it.
Label is for a burgundy style bottle with a label height of 3.5 - 4" and a width of 3.5-4"
any label <= 4"x4" and >=3.5"x3.5" will be acceptable:
HOWEVER Width should be greater than or equal to height due to the bottle format
Target Market(s)
Wine enthusiasts with adequate discretionary budgets to afford $100 bottles of wine.
Industry/Entity Type
Wine / Winery
Requirements
Must have
- A sense of luxury, a feel of exclusivity, and a theme consistent with our product and brand name
Nice to have
- Tree line, wood grain or other wood themes. Serif fonts
Should not have
- anything cheesy, off topic, hard to read script fonts or anything that makes the label hard to read from a few feet away or too busy

```html
<!DOCTYPE html>
<html lang="en">
<head>
<meta charset="utf-8">
<title>Harrowgate Vineyards — Syrah Label</title>
<link href="https://fonts.googleapis.com/css2?family=Josefin+Sans:wght@300&family=Cormorant+SC:wght@600&display=swap" rel="stylesheet">
<style>
  :root {
    --page: #ffffff;
    --label-black: #0d0d0d;
    --rule-silver: #a9a9a9;
    --gold-light: #f2dc8a;
    --gold: #c9a13f;
    --gold-deep: #8f6a1e;
    --wood-dark: #2b1d12;
    --wood-mid: #4a3422;
    --ink-light: #e4e2de;
  }
  * { margin: 0; padding: 0; box-sizing: border-box; }
  html, body { width: 1200px; height: 1020px; overflow: hidden; background: var(--page); }
  .canvas { position: relative; width: 1200px; height: 1020px; }

  .front-label {
    position: absolute; left: 223px; top: 56px;
    width: 754px; height: 657px;
    background: var(--label-black);
  }
  .front-label .rule {
    position: absolute; left: 24px; right: 24px; height: 4px;
    background: var(--rule-silver);
  }
  .front-label .rule--top { top: 10px; }
  .front-label .rule--bottom { bottom: 10px; }

  .brand-name {
    position: absolute; left: 0; right: 0;
    text-align: center;
    font-family: "Josefin Sans", sans-serif;
    font-weight: 300;
    color: var(--gold);
    text-transform: uppercase;
    line-height: 1;
  }
  .brand-name__main { top: 258px; font-size: 74px; letter-spacing: 2px; }
  .brand-name__sub { top: 372px; font-size: 40px; letter-spacing: 7px; }

  .region {
    position: absolute; left: 0; right: 0; top: 565px;
    text-align: center;
    font-family: "Josefin Sans", sans-serif;
    font-weight: 300;
    font-size: 34px;
    letter-spacing: 3px;
    color: var(--ink-light);
  }

  .varietal-strip {
    position: absolute; left: 223px; top: 801px;
    width: 754px; height: 162px;
  }
  .varietal-strip .wood {
    position: absolute; inset: 0;
    background: linear-gradient(90deg, var(--wood-dark) 0%, var(--wood-mid) 30%, var(--wood-dark) 55%, var(--wood-mid) 80%, var(--wood-dark) 100%);
  }
  .varietal-strip .gold-rule {
    position: absolute; left: 38px; right: 38px; height: 6px;
    background: linear-gradient(90deg, var(--gold-deep), var(--gold-light), var(--gold), var(--gold-light), var(--gold-deep));
  }
  .varietal-strip .gold-rule--top { top: 7px; }
  .varietal-strip .gold-rule--bottom { bottom: 7px; }

  .varietal {
    position: absolute; left: 0; right: 0; top: 34px;
    text-align: center;
    font-family: "Josefin Sans", sans-serif;
    font-weight: 300;
    font-size: 56px;
    line-height: 1;
    color: var(--ink-light);
  }
  .vintage-line {
    position: absolute; left: 0; right: 0; top: 99px;
    text-align: center;
    font-family: "Cormorant SC", serif;
    font-weight: 600;
    font-size: 30px;
    line-height: 1;
    letter-spacing: 3px;
    color: var(--ink-light);
  }
</style>
</head>
<body>
<main class="canvas">
  <section class="front-label">
    <div class="rule rule--top"></div>
    <div class="brand-name brand-name__main">Harrowgate</div>
    <div class="brand-name brand-name__sub">Vineyards</div>
    <div class="region">WILLAMETTE VALLEY</div>
    <div class="rule rule--bottom"></div>
  </section>

  <section class="varietal-strip">
    <div class="wood" role="img" aria-label="Dark walnut wood grain background"></div>
    <div class="gold-rule gold-rule--top"></div>
    <div class="varietal">SYRAH</div>
    <div class="vintage-line">ESTATE | 2023 | GROWN</div>
    <div class="gold-rule gold-rule--bottom"></div>
  </section>
</main>
</body>
</html>
```